Stationery Design Project - Red Anvil Workforce

Red Anvil Workforce Staff
*Perth *Brisbane

Business Cards
Size: 90mm x 55mm
Letterhead
Size: A4 - 210mm x 297mm
With Compliments Slip
Size: DL - 210mm x 99mm
Notepad
Size: 250mm x 140mm
Presentation Folder
Size: A4

Phone: 08 9471 3826
Email: info@redanvilworkforce.example.com.au
website: www.redanvilworkforce.example.com.au
Address: 417 Tamber Road
Kellmoor Harwick Province 7150

-
Business cards:

Neil Dawson
Managing Director
Phone: 08 9471 3826
Mobile: 0477 863 150
Email: neild@redanvilworkforce.example.com.au
Address: 417 Tamber Road
-
Its a new manpower (Recruitment Agency) that employs blue collar workers eg: fitters, welders, drivers and warehouse people

If you need any further information please contact myself

Cheers

Neil

```html
<!DOCTYPE html>
<html lang="en">
<head>
<meta charset="utf-8">
<title>Red Anvil Workforce – Business Card</title>
<link rel="stylesheet" href="https://fonts.googleapis.com/css2?family=Open+Sans:wght@400;600;700&display=swap">
<style>
  :root {
    --backdrop: #2b2b2d;
    --paper: #f4f4f4;
    --brand-blue: #1f76c2;
    --band-blue: #1aa0dc;
    --card-dark: #2c2c2e;
    --card-dark-deep: #1e1e20;
    --text-light: #e6e6e6;
    --text-muted: #c2c2c4;
    --white: #ffffff;
  }
  * { box-sizing: border-box; margin: 0; padding: 0; }
  html, body {
    width: 1200px; height: 900px; overflow: hidden;
    background: var(--backdrop);
    font-family: "Open Sans", Arial, sans-serif;
  }
  .stage {
    position: relative; width: 1200px; height: 900px;
    display: flex; justify-content: center; align-items: center; gap: 60px;
  }
  .card {
    position: relative; width: 460px; height: 752px; overflow: hidden;
    box-shadow: 0 18px 40px rgba(0,0,0,.55);
  }

  /* Front */
  .card-front { background: var(--paper); }
  .front-brand {
    height: 340px; display: flex; flex-direction: column;
    align-items: center; justify-content: center; gap: 22px;
  }
  .brand-dot {
    width: 78px; height: 78px; border-radius: 50%;
    background: var(--brand-blue);
  }
  .brand-name {
    color: var(--brand-blue); font-weight: 600; text-align: center;
    text-transform: uppercase; letter-spacing: .22em; line-height: 1.35;
  }
  .brand-name .line-main { display: block; font-size: 34px; }
  .brand-name .line-sub { display: block; font-size: 18px; letter-spacing: .3em; }

  .person-band {
    height: 112px; background: var(--band-blue);
    padding: 26px 0 0 40px; color: var(--white);
  }
  .person-name { font-size: 28px; font-weight: 700; line-height: 1.15; }
  .person-title { font-size: 22px; font-weight: 400; line-height: 1.3; }

  .contact-panel {
    height: 300px;
    background: linear-gradient(160deg, var(--card-dark), var(--card-dark-deep));
    padding: 32px 16px 0 34px;
  }
  .contact-list { list-style: none; }
  .contact-item {
    display: flex; align-items: flex-start; gap: 14px;
    color: var(--text-muted); font-size: 17px; line-height: 1.4;
    margin-bottom: 12px; white-space: nowrap;
  }
  .contact-item.address { margin-bottom: 22px; }
  .contact-item .icon {
    flex: 0 0 26px; width: 26px; height: 26px; border-radius: 50%;
    background: var(--band-blue);
    display: flex; align-items: center; justify-content: center;
  }
  .contact-item .icon svg { width: 14px; height: 14px; }

  /* Back */
  .card-back {
    background: linear-gradient(160deg, var(--card-dark), var(--card-dark-deep));
    padding-top: 70px; text-align: center;
  }
  .back-brand {
    color: var(--text-light); font-weight: 600;
    text-transform: uppercase; letter-spacing: .22em; line-height: 1.4;
  }
  .back-brand .line-main { display: block; font-size: 32px; }
  .back-brand .line-sub { display: block; font-size: 17px; letter-spacing: .3em; }
  .locations {
    margin-top: 44px; color: var(--text-light);
    font-size: 26px; font-weight: 400;
  }
  .back-dot {
    position: absolute; right: -70px; bottom: 120px;
    width: 260px; height: 260px; border-radius: 50%;
    background: var(--band-blue);
  }
</style>
</head>
<body>
<main class="stage">

  <section class="card card-front" aria-label="Business card front">
    <header class="front-brand">
      <span class="brand-dot" aria-hidden="true"></span>
      <h1 class="brand-name">
        <span class="line-main">Red Anvil</span>
        <span class="line-sub">Workforce Staff</span>
      </h1>
    </header>

    <div class="person-band">
      <p class="person-name">Neil Dawson</p>
      <p class="person-title">Managing Director</p>
    </div>

    <div class="contact-panel">
      <ul class="contact-list">
        <li class="contact-item address">
          <span class="icon">
            <svg viewBox="0 0 14 14"><path d="M7 1a4 4 0 0 0-4 4c0 3 4 8 4 8s4-5 4-8a4 4 0 0 0-4-4z" fill="#fff"/><circle cx="7" cy="5" r="1.5" fill="#1aa0dc"/></svg>
          </span>
          <span>417 Tamber Road<br>Kellmoor Harwick Province 7150</span>
        </li>
        <li class="contact-item phone">
          <span class="icon">
            <svg viewBox="0 0 14 14"><path d="M3 1.5l2 .3 1 3-1.4 1a7 7 0 0 0 3.6 3.6l1-1.4 3 1 .3 2c-.2.8-1 1.3-1.8 1.3A10 10 0 0 1 1.5 3.3c0-.8.5-1.6 1.5-1.8z" fill="#fff"/></svg>
          </span>
          <span>08 9471 3826</span>
        </li>
        <li class="contact-item mobile">
          <span class="icon">
            <svg viewBox="0 0 14 14"><rect x="4" y="1" width="6" height="12" rx="1.2" fill="#fff"/><rect x="5" y="2.5" width="4" height="7" fill="#1aa0dc"/></svg>
          </span>
          <span>0477 863 150</span>
        </li>
        <li class="contact-item email">
          <span class="icon">
            <svg viewBox="0 0 14 14"><rect x="1.5" y="3" width="11" height="8" rx="1" fill="#fff"/><path d="M1.8 3.5L7 7.5l5.2-4" stroke="#1aa0dc" stroke-width="1.2" fill="none"/></svg>
          </span>
          <span>neild@redanvilworkforce.example.com.au</span>
        </li>
        <li class="contact-item web">
          <span class="icon">
            <svg viewBox="0 0 14 14"><circle cx="7" cy="7" r="5.5" fill="none" stroke="#fff" stroke-width="1.3"/><path d="M1.5 7h11M7 1.5c-2.5 3-2.5 8 0 11M7 1.5c2.5 3 2.5 8 0 11" stroke="#fff" stroke-width="1" fill="none"/></svg>
          </span>
          <span>www.redanvilworkforce.example.com.au</span>
        </li>
      </ul>
    </div>
  </section>

  <section class="card card-back" aria-label="Business card back">
    <h2 class="back-brand">
      <span class="line-main">Red Anvil</span>
      <span class="line-sub">Workforce Staff</span>
    </h2>
    <p class="locations">Kellmoor | Varrington</p>
    <span class="back-dot" aria-hidden="true"></span>
  </section>

</main>
</body>
</html>
```